Anzeige zur Kundenakquise
Zielgruppe
Wir sind der größte unabhängige Versicherungsmakler Deutschlands.
https://www.nordlicht-policenhaus.de/
Aufgabenstellung
Die Anzeige dient zur Kundenakquise. Der Flyer soll in erster Linie auf Chatterly veröffentlicht werden.
Sie soll Kunden anregen eine Nachricht an uns zu schicken und einen Termin bis zum 30.11.2018 zu vereinbaren um ihre KFZ-Versicherungen vergleichen zu lassen.
Der alte Flyer wird mit hochgeladen. Bitte den Text nicht 1 zu 1 übernehmen.
Farbe und Stil sollten übernommen werden.
Die Maße für Chatterly:
Empfohlene Bildgröße:
1.200 x 628 Pixel
Bildseitenverhältnis: 1,91:1
Auf Grund der Zusendung von mehrerern Flyer der Designer bitte ich die Anzahl auf 3 zu einigen, d.h. bitte senden Sie für eine Chatterly Slidekampane 3 Flyer als ein Projekt zu. Vielen Dank für Ihre Mühe.

```html
<!DOCTYPE html>
<html lang="de">
<head>
<meta charset="utf-8">
<title>KFZ-Versicherung wechseln – Nordlicht Policenhaus</title>
<link href="https://fonts.googleapis.com/css2?family=Roboto:wght@400;700;900&display=swap" rel="stylesheet">
<style>
  :root {
    --lime: #8cc21e;
    --lime-light: #b5dc3c;
    --lime-pale: #d4ec7c;
    --ink: #4a4a4a;
    --band: rgba(62, 62, 62, 0.78);
    --white: #ffffff;
  }
  * { margin: 0; padding: 0; box-sizing: border-box; }
  html, body { width: 1200px; height: 628px; overflow: hidden; background: var(--white); }
  .ad {
    position: relative;
    width: 1200px;
    height: 628px;
    font-family: "Roboto", Arial, sans-serif;
    overflow: hidden;
    background: var(--white);
  }
  .hero-photo {
    position: absolute;
    left: 0; top: 0;
    width: 1200px; height: 500px;
    background:
      radial-gradient(ellipse at 72% 45%, var(--lime-pale) 0%, rgba(212,236,124,0) 45%),
      linear-gradient(100deg, var(--lime-light) 0%, #a8d334 40%, #c2e25a 75%, var(--lime-light) 100%);
  }
  .band {
    position: absolute;
    left: 0; top: 192px;
    width: 1200px; height: 181px;
    background: var(--band);
  }
  .deadline {
    position: absolute;
    left: 214px; top: 58px;
    font-weight: 900;
    font-size: 56px;
    line-height: 1;
    color: var(--ink);
    letter-spacing: 0.5px;
  }
  .deadline-sub {
    position: absolute;
    left: 215px; top: 129px;
    font-weight: 700;
    font-size: 32px;
    line-height: 1;
    color: var(--white);
  }
  .headline {
    position: absolute;
    left: 212px; top: 222px;
    font-size: 70px;
    line-height: 1;
    color: var(--white);
    font-weight: 400;
    white-space: nowrap;
  }
  .headline .accent { color: var(--lime); font-weight: 900; }
  .headline-sub {
    position: absolute;
    left: 418px; top: 300px;
    font-weight: 700;
    font-size: 26px;
    line-height: 1;
    color: var(--white);
  }
  .savings-badge {
    position: absolute;
    left: 826px; top: 308px;
    width: 220px; height: 220px;
  }
  .cta {
    position: absolute;
    left: 0; top: 544px;
    width: 1200px;
    text-align: center;
    font-weight: 900;
    font-size: 38px;
    line-height: 1;
    color: var(--ink);
  }
  .cta .accent { color: var(--lime); }
  .brand {
    position: absolute;
    left: 1086px; top: 536px;
    display: flex;
    align-items: center;
    gap: 6px;
  }
  .brand-mark { width: 14px; height: 14px; background: var(--ink); }
  .brand-name {
    font-weight: 700;
    font-size: 12px;
    line-height: 1.1;
    color: var(--ink);
    width: 80px;
  }
</style>
</head>
<body>
<div class="ad">
  <div class="hero-photo" role="img" aria-label="Foto einer lächelnden Frau mit Sonnenbrille am Steuer eines Cabrios, grün eingefärbt"></div>
  <div class="band"></div>

  <p class="deadline">BIS ZUM 30.11</p>
  <p class="deadline-sub">KFZ-VERSICHERUNG WECHSELN</p>

  <h1 class="headline"><span class="accent">SCHLUSS</span> MIT TEUREN</h1>
  <p class="headline-sub">KFZ-VERSICHERUNGEN</p>

  <svg class="savings-badge" viewBox="0 0 220 220" aria-label="Bis zu 40% sparen">
    <circle cx="110" cy="110" r="106" fill="var(--lime)"/>
    <circle cx="108" cy="107" r="94" fill="var(--white)"/>
    <g transform="rotate(-14 108 107)" font-family="Roboto, Arial, sans-serif" font-weight="900" fill="var(--lime)" text-anchor="middle">
      <text x="108" y="62" font-size="24">BIS ZU</text>
      <text x="108" y="138" font-size="76">40%</text>
      <text x="108" y="172" font-size="24">SPAREN!</text>
    </g>
  </svg>

  <p class="cta">VEREINBAREN SIE <span class="accent">GLEICH</span> EINEN TERMIN!</p>

  <div class="brand">
    <span class="brand-mark"></span>
    <span class="brand-name">NORDLICHT POLICENHAUS</span>
  </div>
</div>
</body>
</html>
```